A modern and fresh looking church website

Holy Fenwick’s is looking for a new site design for their church. The church is a part of a group of the ‘Corvane Fellowship’ Australia and needs to kind of tie into their branding within reason.
This means, we would need to use the logo colours (Blue, Gold, Red) throughout the website and the design needs to be fresh, modern, clean, and mobile-friendly. The front page must have the following as features:
• Sermons (Podcasts and Videos)
• Events
• Venue Hire (Weddings)
The website will be mainly information-based and will have a few forms. From our recent engagement with the church, I did draft up a mock-up design for them and even it looks better than their current site, it’s not giving a ‘stand out impression’ and has that out of date look.
The inner pages will be based off the front-page design so we will take care of that, we are just looking for a front-page design that is unique and has the wow factor.
The website will be coded by our in-house development team and will be coded in a WordPress format using Elementor pro.
We are looking for a couple of designers to design 1-3 mock-ups by taking our current draft and putting their spin to it.
Updates
Hi,
Due to Christmas and the client was on leave, the design selection has been delayed. It was not ideal as I knew this would happen.
I made contact with the client and just been told that the client is leaving the church and a handover is happening for the new staff member. The new staff member will present all designs to the board for selection. This is due to be completed by the first week of February 2021.
We thanks for your patients as this was not expected and we seeing if we can hurry this process up.

```html
<!DOCTYPE html>
<html lang="en">
<head>
<meta charset="utf-8">
<title>Holy Fenwick’s Perth – Home</title>
<link rel="stylesheet" href="https://fonts.googleapis.com/css2?family=Montserrat:wght@300;400;500;600;700&family=Libre+Baskerville:wght@400;700&family=Arimo:wght@400;700&display=swap">
<style>
:root{
  --page-bg:#f5f5f5;
  --white:#ffffff;
  --blue:#0a5eb4;
  --blue-bar:#3a7fc7;
  --red:#cc2229;
  --gold:#9e7c30;
  --card-grey:#e7e7e7;
  --ink:#3c3c3c;
  --nav-grey:#7d7d7d;
  --blurb:#8a8a8a;
  --panel:#1d2a3b;
}
*{margin:0;padding:0;box-sizing:border-box}
html,body{width:1200px;height:2277px;overflow:hidden}
body{position:relative;background:var(--page-bg);font-family:"Montserrat",sans-serif;color:var(--ink)}
.abs{position:absolute}
.site{left:116px;top:108px;width:968px;height:2036px;background:var(--white);box-shadow:0 12px 28px rgba(0,0,0,.28)}

/* header */
.topbar{left:116px;top:108px}
.contact-item{top:118px;display:flex;align-items:center;gap:10px;color:var(--white);font-size:10px;font-weight:500}
.contact-icon{width:19px;height:19px}
.brand{left:154px;top:141px;height:50px;display:flex;align-items:center;gap:10px}
.brand-dot{width:44px;height:44px;border-radius:50%;background:var(--blue)}
.brand-name{font-size:27px;font-weight:700;color:var(--blue);letter-spacing:.2px}
.main-nav{left:489px;top:172px;width:560px;display:flex;justify-content:space-between;font-size:13px;font-weight:500;color:var(--nav-grey);letter-spacing:.4px}
.main-nav .current{color:var(--red)}

/* hero */
.hero{left:116px;top:208px;width:968px;height:552px;
  background:
   radial-gradient(ellipse 55% 35% at 55% 95%,rgba(230,215,190,.9),rgba(200,170,130,0) 70%),
   radial-gradient(ellipse 40% 30% at 25% 85%,rgba(215,195,165,.85),rgba(0,0,0,0) 70%),
   radial-gradient(ellipse 20% 18% at 55% 14%,rgba(90,130,200,.6),rgba(0,0,0,0) 70%),
   linear-gradient(180deg,#4a2a1c 0%,#6b3d25 35%,#8a6a4c 70%,#b89c7a 100%)}
.hero-title{left:116px;top:330px;width:968px;text-align:center;font-family:"Libre Baskerville",serif;font-weight:700;font-size:50px;color:var(--white);letter-spacing:1px}
.hero-title span{border-bottom:3px solid var(--white);padding-bottom:0}
.hero-time{left:116px;width:968px;text-align:center;font-weight:600;font-size:42px;color:var(--white);letter-spacing:1px;text-shadow:0 2px 4px rgba(0,0,60,.55)}

/* feature cards */
.feature{top:680px;width:262px;height:363px}
.feature-dome{left:78px;top:0;width:106px;height:60px;border-radius:53px 53px 0 0}
.feature-head{left:0;top:32px;width:262px;height:79px;display:flex;align-items:center;justify-content:center;font-family:"Libre Baskerville",serif;font-size:31px;color:var(--white);letter-spacing:1px;box-shadow:0 4px 8px rgba(0,0,0,.25)}
.feature-photo{left:0;top:111px;width:262px;height:122px}
.feature-body{left:0;top:233px;width:262px;height:130px;background:var(--card-grey)}
.feature-blurb{left:19px;top:15px;width:228px;font-family:"Arimo",sans-serif;font-size:7.6px;line-height:12.4px;color:var(--blurb)}
.feature-blurb b{color:#6e6e6e}
.feature-btn{left:65px;top:78px;width:133px;height:34px;border:2px solid;display:flex;align-items:center;justify-content:center;font-size:12px;font-weight:500;letter-spacing:1px;background:transparent}
.sermons .bg{background:var(--blue)} .sermons .feature-btn{color:var(--blue);border-color:var(--blue)}
.events .bg{background:var(--red)} .events .feature-btn{color:var(--red);border-color:var(--red)}
.weddings .bg{background:var(--gold)} .weddings .feature-btn{color:var(--gold);border-color:var(--gold)}

/* welcome */
.welcome-title{left:116px;top:1116px;width:968px;text-align:center;font-size:37px;font-weight:600;letter-spacing:3px;color:#454545}
.welcome-sub{left:116px;top:1178px;width:968px;text-align:center;font-size:30px;font-weight:600;letter-spacing:3px;color:#454545}
.welcome-text{left:210px;top:1248px;width:780px;text-align:center;font-size:23px;font-weight:300;line-height:48px;color:#3a3a3a}

/* info panels */
.panel{top:1719px;width:427px;height:259px;background:
  radial-gradient(ellipse 60% 60% at 70% 40%,rgba(60,75,95,.6),rgba(0,0,0,0) 70%),var(--panel)}
.location-title{left:0;top:24px;width:427px;text-align:center;font-size:20px;font-weight:700;color:var(--white)}
.map{left:27px;top:72px;width:191px;height:162px;border:2px solid var(--blue-bar);background:linear-gradient(135deg,#e8e4d8,#d9e3ea 60%,#e6dfcf)}
.loc-row{left:238px;display:flex;align-items:flex-start;gap:8px;color:var(--white);font-size:10px;font-weight:500;line-height:18px;letter-spacing:.4px}
.loc-row svg{flex:none;width:21px;height:21px}
.hours{left:236px;top:195px;color:var(--white);font-size:11px;font-weight:600;line-height:18px}
.give-title{left:0;top:36px;width:427px;text-align:center;font-size:30px;font-weight:700;color:var(--white)}
.give-text{left:60px;top:98px;width:307px;text-align:center;font-family:"Arimo",sans-serif;font-size:11.5px;line-height:21px;color:var(--white)}
.give-btn{left:123px;top:193px;width:181px;height:41px;border:2px solid var(--white);display:flex;align-items:center;justify-content:center;color:var(--white);font-size:18px;font-weight:400;letter-spacing:.5px}

/* footer */
.footer{left:116px;top:2006px;width:968px;height:138px;background:var(--blue)}
.footer-brand{left:168px;top:2048px;width:130px;text-align:center;font-size:16px;font-weight:700;color:var(--white);line-height:20px}
.footer-nav{left:311px;top:2052px;width:710px;display:flex;justify-content:space-between;font-size:17px;font-weight:500;color:var(--white);letter-spacing:.4px}
.footer-rule{left:320px;top:2093px;width:696px;height:1px;background:rgba(255,255,255,.7)}
.copyright{left:116px;top:2116px;width:1220px;padding-right:252px;text-align:center;font-size:13px;color:var(--white)}
</style>
</head>
<body>
<div class="abs site"></div>

<header>
  <svg class="abs topbar" width="968" height="34" viewBox="0 0 968 34">
    <rect x="0" y="0" width="968" height="3" fill="#3a7fc7"/>
    <path d="M330 0 C372 0 368 34 410 34 H968 V0 Z" fill="#3a7fc7"/>
  </svg>
  <div class="abs contact-item" style="left:580px">
    <svg class="contact-icon" viewBox="0 0 20 20"><circle cx="10" cy="10" r="9" fill="none" stroke="#fff" stroke-width="1.3"/></svg>social/holyfenwicks
  </div>
  <div class="abs contact-item" style="left:760px">
    <svg class="contact-icon" viewBox="0 0 20 20"><circle cx="10" cy="10" r="9" fill="none" stroke="#fff" stroke-width="1.3"/><path d="M7 6 l2 0 l1 2.5 l-1.3 1 a6 6 0 0 0 2.8 2.8 l1-1.3 l2.5 1 l0 2 a1 1 0 0 1-1 1 A8 8 0 0 1 6 7 a1 1 0 0 1 1-1z" fill="#fff"/></svg>(07) 4000 1234
  </div>
  <div class="abs contact-item" style="left:899px">
    <svg class="contact-icon" viewBox="0 0 20 20"><circle cx="10" cy="10" r="9" fill="none" stroke="#fff" stroke-width="1.3"/><rect x="5.5" y="7" width="9" height="6.5" fill="#fff"/><path d="M5.5 7 L10 10.5 L14.5 7" fill="none" stroke="#3a7fc7" stroke-width="1"/></svg>office@corvane.org.au
  </div>
  <div class="abs brand"><span class="brand-dot"></span><span class="brand-name">Holy Fenwick’s</span></div>
  <nav class="abs main-nav">
    <span class="current">Home</span><span>About Us</span><span>Services</span><span>Sermons</span><span>Events</span><span>Weddings</span><span>Contact Us</span>
  </nav>
</header>

<section>
  <div class="abs hero" role="img" aria-label="Photo of an open Bible in a softly lit church interior with stained glass and pews"></div>
  <h1 class="abs hero-title"><span>Service&nbsp; Times</span></h1>
  <p class="abs hero-time" style="top:407px">SATURDAY 6:00 PM</p>
  <p class="abs hero-time" style="top:476px">SUNDAY 08:30 AM &amp; 10:20 AM</p>
</section>

<section>
  <article class="abs feature sermons" style="left:182px">
    <div class="abs feature-dome bg"></div>
    <h2 class="abs feature-head bg">Sermons</h2>
    <div class="abs feature-photo" role="img" aria-label="Photo of headphones and a phone on a table" style="background:linear-gradient(160deg,#f3d9c4,#e9c7b0 50%,#6f7480)"></div>
    <div class="abs feature-body">
      <p class="abs feature-blurb"><b>Lorem Ipsum</b> text is simply placeholder (or ‘dummy’) text that is frequently used by designers, publishers, printers and typesetters when developing new content layouts for web and print.</p>
      <span class="abs feature-btn">Learn More</span>
    </div>
  </article>
  <article class="abs feature events" style="left:468px">
    <div class="abs feature-dome bg"></div>
    <h2 class="abs feature-head bg">Events</h2>
    <div class="abs feature-photo" role="img" aria-label="Photo of a congregation gathered at a worship event" style="background:linear-gradient(180deg,#5b4a66,#3b2f49 45%,#7a5a6a)"></div>
    <div class="abs feature-body">
      <p class="abs feature-blurb"><b>Lorem Ipsum</b> text is simply placeholder (or ‘dummy’) text that is frequently used by designers, publishers, printers and typesetters when developing new content layouts for web and print.</p>
      <span class="abs feature-btn">Learn More</span>
    </div>
  </article>
  <article class="abs feature weddings" style="left:755px">
    <div class="abs feature-dome bg"></div>
    <h2 class="abs feature-head bg">Weddings</h2>
    <div class="abs feature-photo" role="img" aria-label="Photo of a wedding ceremony at a church altar" style="background:linear-gradient(180deg,#c9a85a,#8e6d36 45%,#d8d0c2)"></div>
    <div class="abs feature-body">
      <p class="abs feature-blurb"><b>Lorem Ipsum</b> text is simply placeholder (or ‘dummy’) text that is frequently used by designers, publishers, printers and typesetters when developing new content layouts for web and print.</p>
      <span class="abs feature-btn">Learn More</span>
    </div>
  </article>
</section>

<section>
  <h2 class="abs welcome-title">WELCOME TO HOLY FENWICK’S PERTH</h2>
  <h3 class="abs welcome-sub">CORVANE FELLOWSHIP</h3>
  <p class="abs welcome-text">Lorem ipsum dolor sit amet, consectetur adipiscing elit. Duis sollicitudin felis ac massa pellentesque pharetra. Ut ut metus id risus porttitor fringilla id non nibh. Maecenas a metus id ex luctus ultrices ac et justo. Duis malesuada congue scelerisque. Ut accumsan venenatis massa, vitae sodales lectus luctus sit amet. Morbi auctor, ipsum vitae porta mollis, diam dui tempor lacus, at mattis eros lacus eget arcu. Ut et tortor ornare, lacinia diam scelerisque, tempor elit.</p>
</section>

<section>
  <div class="abs panel" style="left:144px">
    <h2 class="abs location-title">OUR LOCATION</h2>
    <div class="abs map" role="img" aria-label="Street map of central Perth showing the church location"></div>
    <div class="abs loc-row" style="top:72px">
      <svg viewBox="0 0 20 20"><circle cx="10" cy="8" r="6" fill="none" stroke="#fff" stroke-width="2"/><path d="M7 15 L10 19 L13 15 Z" fill="#fff"/></svg>
      <span>22 Marlow Street<br>Perth, WA 6000</span>
    </div>
    <div class="abs loc-row" style="top:122px">
      <svg viewBox="0 0 20 20"><circle cx="10" cy="10" r="9" fill="none" stroke="#fff" stroke-width="1.3"/><path d="M7 6 l2 0 l1 2.5 l-1.3 1 a6 6 0 0 0 2.8 2.8 l1-1.3 l2.5 1 l0 2 a1 1 0 0 1-1 1 A8 8 0 0 1 6 7 a1 1 0 0 1 1-1z" fill="#fff"/></svg>
      <span>51 00 00 00</span>
    </div>
    <div class="abs loc-row" style="top:157px">
      <svg viewBox="0 0 20 20"><circle cx="10" cy="10" r="9" fill="none" stroke="#fff" stroke-width="1.3"/><rect x="5.5" y="7" width="9" height="6.5" fill="#fff"/><path d="M5.5 7 L10 10.5 L14.5 7" fill="none" stroke="#1d2a3b" stroke-width="1"/></svg>
      <span>hello@holyfenwick.org.au</span>
    </div>
    <p class="abs hours">Office Hours<br>Tuesday, Thursday and Friday<br>09.00 AM - 04.00 PM</p>
  </div>
  <div class="abs panel" style="left:625px" role="group" aria-label="Give today">
    <h2 class="abs give-title">GIVE TODAY</h2>
    <p class="abs give-text">Lorem ipsum dolor sit amet, consectetur adipiscing elit. Duis sollicitudin felis ac massa pellentesque pharetra. Ut ut metus id risus porttitor fringilla id non nibh</p>
    <span class="abs give-btn">MAKE A GIFT</span>
  </div>
</section>

<footer>
  <div class="abs footer"></div>
  <p class="abs footer-brand">Holy Fenwick’s</p>
  <nav class="abs footer-nav">
    <span>Home</span><span>About Us</span><span>Services</span><span>Sermons</span><span>Events</span><span>Weddings</span><span>Contact Us</span>
  </nav>
  <div class="abs footer-rule"></div>
  <p class="abs copyright" style="left:320px;width:696px;padding:0">©2020 &nbsp;|&nbsp; holyfenwick.org.au &nbsp;|&nbsp; Allright&nbsp; Reserved</p>
</footer>
</body>
</html>
```